Etiketten für Nahrungsergänzung für Tiere
Zielgruppe
Wir stellen kolloidale Mischungen für Tiere her. Dies sind grob gesagt Nahrungsmittelergänzungen. Die Zielgruppe sind Tierbesitzer bzw. gesundheitsbewusste Menschen.
Aufgabenstellung
natürlich, in braun, beige, gold oder hellblau Tönen. Das Etikett wird auf eine Flasche aufgebraucht in der sich eine Flüssigkeit befindet. Das Etikett ist breiter als hoch. 115 x 61 mm (B x H)
Bisher haben wir blaue Flaschen verwendet und waren dadurch mit der Farbgebung ehr kühl und reduziert. In Zukunft wollen wir braune Flaschen mit schwarzen Deckel verwendet. Damit darf die Farbgebung auch wärmer, natürlich und das Etikett auch mit mehr Details versehen werden.
In den Uploads füge ich das aktuell Logo hinzu. Dies verwenden wir in braun/gold und in grün. Falls sich diese Gestaltung nicht so günstig auswirkt, haben wir ein 'alternative' Logo hinzugefügt. Da die Seite nächstes Jahr komplett überarbeitet wird und unsere Firma sich vergrößert, kann diese Änderung durchgeführt werden.
Ich lade noch ein Etikett hoch, welches wir für die Einzelelemente nutzen. Hier sind und bleiben die Flaschen nach wir vor blau (Herstellervorgaben), dadurch sind die Etikett sehr kühl und reduziert. Das darf auf den Entwurf für die Mischungen sehr gern deutlich verändert werden :-)

```html
<!DOCTYPE html>
<html lang="de">
<head>
<meta charset="utf-8">
<title>Etikett Kolloidale Mischung</title>
<link rel="stylesheet" href="https://fonts.googleapis.com/css2?family=Pathway+Gothic+One&family=Cinzel:wght@700&display=swap">
<style>
  :root {
    --stage: #e7e5e7;
    --paper: #fbf8f1;
    --paper-front: #fdfcf8;
    --box-fill: #f6efe2;
    --box-line: #d8c6a2;
    --band: #ebe1cc;
    --ink: #2a2622;
    --orange: #e2740f;
    --gold: #b08c12;
    --gold-light: #d6b52a;
    --swirl: #efe7d2;
  }
  * { margin: 0; padding: 0; box-sizing: border-box; }
  html, body {
    width: 1200px; height: 1171px; overflow: hidden;
    background: var(--stage);
    font-family: "Pathway Gothic One", sans-serif;
    color: var(--ink);
  }
  .label {
    position: absolute; left: 50px; top: 200px;
    width: 1100px; height: 769px;
    display: flex;
    box-shadow: 0 10px 30px rgba(0,0,0,.12);
  }
  .label-band {
    position: absolute; left: 0; top: 0; right: 0; height: 17px;
    background: var(--band); z-index: 2;
  }
  .panel { position: relative; height: 100%; }
  .panel-back { width: 544px; background: var(--paper); }
  .panel-front {
    width: 556px;
    background: linear-gradient(90deg, #f2f1ee 0%, var(--paper-front) 12%, #ffffff 50%, var(--paper-front) 88%, #efeeea 100%);
    text-align: center;
    overflow: hidden;
  }
  .notes {
    position: absolute; left: 22px; top: 41px; width: 503px; height: 472px;
    background: var(--box-fill);
    border: 2px solid var(--box-line);
    text-align: center;
    padding-top: 12px;
    font-size: 23px; line-height: 31px;
  }
  .notes h2 {
    font-weight: 400; font-size: 40px; line-height: 46px;
    color: var(--orange); margin-bottom: 4px;
  }
  .notes p { margin-bottom: 8px; }
  .meta { position: absolute; top: 532px; font-size: 24px; }
  .meta-date { left: 34px; }
  .meta-batch { left: 355px; }
  .maker {
    position: absolute; left: 154px; top: 620px;
    font-size: 25px; line-height: 31px;
  }
  .maker .web { color: var(--orange); font-size: 30px; line-height: 40px; }
  .swirl-area {
    position: absolute; left: 30px; top: 230px; width: 560px; height: 560px;
    border-radius: 50%;
    background: radial-gradient(circle, rgba(239,231,210,.55) 0%, rgba(239,231,210,.35) 55%, rgba(239,231,210,0) 72%);
  }
  .brand {
    position: absolute; left: 0; right: 0; top: 120px;
    font-size: 42px; letter-spacing: 8px; color: var(--ink);
  }
  .product {
    position: absolute; left: 0; right: 0; top: 252px;
    font-family: "Cinzel", serif; font-weight: 700;
    font-size: 60px; line-height: 76px; letter-spacing: 2px;
    color: var(--gold);
    background: linear-gradient(180deg, var(--gold-light), var(--gold));
    -webkit-background-clip: text; background-clip: text;
    -webkit-text-fill-color: transparent;
  }
  .volume {
    position: absolute; left: 0; right: 0; top: 680px;
    font-size: 42px; letter-spacing: 2px;
  }
</style>
</head>
<body>
  <div class="label">
    <div class="label-band"></div>
    <section class="panel panel-back">
      <div class="notes">
        <h2>Hinweise:</h2>
        <p>Bei Raumtemperatur und lichtgeschützt lagern.</p>
        <p>Vor Mikrowellen und magnetischen Feldern fernhalten.</p>
        <p>PPM-Messmethode: Atomspektralanalyse<br>Anwendung nach dem Quantenprinzip der verschränkten<br>Teilchen.</p>
        <p>Nicht für den menschlichen Verzehr geeignet.</p>
        <p>Protonenresonanzverfahren mind. 99,95%<br>reine kolloidale Elemente in doppelt destilliertem<br>Wasser.</p>
        <p>Mischung aus kolloidalen Mengen- und Spuerenelementen.</p>
        <p>Außerhalb der Reichweite von Kindern aufbewahren.</p>
      </div>
      <div class="meta meta-date">Mindestens haltbar bis:</div>
      <div class="meta meta-batch">Charge:</div>
      <div class="maker">
        Johanna Weidner<br>
        Am Wiesengrund 12 - 98765 Lindenthal<br>
        <span class="web">www.tierquell-kolloide.de</span>
      </div>
    </section>
    <section class="panel panel-front">
      <div class="swirl-area" role="img" aria-label="Dezente beige Spirale als Hintergrundornament"></div>
      <div class="brand">TIERQUELL</div>
      <h1 class="product">KOLLODIALE<br>MISCHUNG</h1>
      <div class="volume">50 ML</div>
    </section>
  </div>
</body>
</html>
```